Marrowfield Biomedical Research Institute (MBRX) Web Design

MBRX is a non-profit organization focused on saving the lives of terminally ill patients by becoming the leaders in cutting-edge research, innovative technologies, utilizing national and international partnerships as well as the associated allopathic and naturopathic treatments necessary to do so.

Our primary focus is raising funds to support the research and acquisition of new technologies for life saving treatments which are NOT a one size fits all approach like conventional medicine but rather a marriage of the latest technologies used in combination with other new treatment possibilities for a successful end result.

Our domain is marrowfieldbrx.org

Logo files are attached.

Looking for something clean, light, healthy.

Target Market(s)

The site should look and feel towards research/scientific grant writing.
Medical professionals, Medical Scientists.

Industry/Entity Type

Medical And Science

Number of Pages Required

4 page

Requirements
Nice to have
• Here are examples of sites I like in the order of how much I like them.
• https://www.palvenhope.org/give.html
• https://www.thekqtf.org/donate-to-kqtf
• https://www.velmorecure.org/we-are-vci/join-the-cause
• https://www.tumarex.org/involved/donate.html
• https://give.dwkt.org/checkout/donation?eid=58217
• https://www.quillavent.org/how-you-can-help
• https://donate3.tumarex.org/

```html
<!DOCTYPE html>
<html lang="en">
<head>
<meta charset="utf-8">
<title>Marrowfield Biomedical Research Institute — Donate</title>
<link href="https://fonts.googleapis.com/css2?family=Poppins:wght@300;400;500;600&display=swap" rel="stylesheet">
<style>
:root{
  --green:#5aa937;
  --green-dark:#3f8a22;
  --blue:#1b75bb;
  --ink:#222831;
  --muted:#6d737a;
  --line:#e3e6ea;
  --pale:#f3f7f8;
  --footer:#2b3036;
  --footer-field:#383e45;
  --social:#9aa3ab;
  --white:#ffffff;
}
*{box-sizing:border-box;margin:0;padding:0}
html,body{width:1200px;height:4478px;overflow:hidden}
body{font-family:'Poppins',sans-serif;color:var(--ink);background:var(--white);font-size:14px}
a{color:inherit;text-decoration:none}
.heading{font-size:30px;font-weight:500;text-align:center;line-height:1.25}
.heading-rule{width:36px;height:2px;background:var(--green);margin:14px auto 0}
.btn{display:inline-flex;align-items:center;justify-content:center;font-size:11px;font-weight:600;text-transform:uppercase;height:40px;padding:0 26px;letter-spacing:.3px;white-space:nowrap}

/* top bar */
.topbar{height:42px;display:flex;align-items:center;justify-content:space-between;padding:0 90px;font-size:12px;color:var(--muted);border-bottom:1px solid var(--line);white-space:nowrap}
.topbar-left,.topbar-right{display:flex;gap:30px;align-items:center}
.topbar span{display:flex;align-items:center;gap:6px}
.dot{width:10px;height:10px;border-radius:50%;background:#9aa0a6;display:inline-block}

/* nav */
.nav{height:78px;display:flex;align-items:center;justify-content:space-between;padding:0 90px;white-space:nowrap}
.brand{display:flex;align-items:center;gap:10px;font-size:26px;font-weight:600;color:var(--blue);flex:none}
.brand-mark{width:30px;height:30px;border-radius:50%;background:var(--green);flex:none}
.menu{display:flex;align-items:center;gap:22px;font-size:11px;font-weight:600;text-transform:uppercase;flex:none}
.menu svg{flex:none}
.my-donation{background:var(--green);color:var(--white);border-radius:20px;padding:8px 16px;font-size:11px;text-transform:none;white-space:nowrap}

/* hero */
.hero{position:relative;height:530px;background:linear-gradient(115deg,#3b2b22 0%,#8c6a52 35%,#c9a98e 55%,#6a4c3a 80%,#2e2019 100%);color:var(--white);text-align:center}
.hero-title{position:absolute;top:185px;left:0;right:0;font-size:42px;font-weight:500;line-height:1.25}
.hero .btn{position:absolute;top:300px;left:50%;transform:translateX(-50%);background:var(--green);height:38px;font-size:10px}
.hero-dots{position:absolute;right:42px;top:250px;display:flex;flex-direction:column;gap:8px}
.hero-dots i{width:6px;height:6px;border-radius:50%;background:rgba(255,255,255,.6)}
.hero-dots i:first-child{background:#fff}
.hero-curve{position:absolute;bottom:-1px;left:50%;transform:translateX(-50%)}

/* how it works */
.how{height:430px;padding-top:85px}
.steps{display:flex;justify-content:space-between;width:880px;margin:70px auto 0;position:relative}
.step{width:240px;text-align:center}
.step svg{display:block;margin:0 auto}
.step h3{font-size:13px;font-weight:600;text-transform:uppercase;margin-top:22px}
.step p{font-size:12px;color:var(--muted);line-height:1.7;margin-top:10px}
.connector{position:absolute;top:28px;width:140px;height:1px;background:var(--line)}

/* ways */
.ways{height:741px;background:var(--pale);padding-top:70px}
.cards{display:flex;gap:27px;justify-content:center;margin-top:60px}
.card{width:322px;height:412px;background:var(--white);position:relative}
.card-photo{height:257px}
.card h3{font-size:16px;font-weight:500;margin:32px 22px 0;padding-left:14px;border-left:3px solid var(--blue);line-height:1.2}
.card p{font-size:12px;color:var(--muted);line-height:1.7;margin:12px 22px 0}
.card-arrow{position:absolute;left:140px;top:108px;width:40px;height:40px;border-radius:50%;background:var(--white);display:flex;align-items:center;justify-content:center}
.ways .btn{display:flex;width:236px;margin:58px auto 0;background:var(--blue);color:var(--white);font-size:10px;padding:0 16px}

/* faq */
.faq{height:642px;padding-top:72px}
.faq-grid{display:grid;grid-template-columns:498px 498px;gap:18px 24px;justify-content:center;margin-top:70px}
.faq-item{border:1px solid var(--line);height:150px;padding:26px 24px 0 58px;position:relative}
.faq-item::before{content:"?";position:absolute;left:24px;top:26px;width:20px;height:20px;border-radius:50%;background:#e6eef7;color:var(--blue);font-size:11px;font-weight:600;display:flex;align-items:center;justify-content:center}
.faq-item h3{font-size:14px;font-weight:500}
.faq-item p{font-size:12px;color:var(--muted);line-height:1.75;margin-top:8px}
.faq-actions{display:flex;gap:16px;justify-content:center;margin-top:42px}
.faq-actions .more{background:#e6eef7;color:var(--blue);font-size:10px}
.faq-actions .ask{background:var(--green);color:var(--white);font-size:10px}

/* donate online */
.donate{position:relative;height:558px;background:linear-gradient(100deg,#9aa39f 0%,#c8c6bd 30%,#8b7561 50%,#d3d5d0 75%,#eef0ec 100%)}
.donate-box{position:absolute;left:788px;top:95px;width:322px;height:373px;background:var(--white);padding:44px 40px 0;box-shadow:0 8px 30px rgba(0,0,0,.08)}
.donate-box h2{font-size:26px;font-weight:500}
.donate-box .heading-rule{margin:14px 0 0}
.donate-box p{font-size:12px;color:var(--muted);line-height:1.75;margin-top:18px}
.donate-box p+p{margin-top:8px}
.donate-box .btn{margin-top:24px;background:#e6eef7;color:var(--blue);height:36px;font-size:10px}

/* helping */
.helping{height:665px;padding-top:76px}
.map{width:880px;height:330px;margin:38px auto 0;background:radial-gradient(ellipse at center,#e3f0dc 0%,#f3f8f0 55%,#ffffff 80%)}
.social{display:flex;gap:70px;justify-content:center;margin-top:60px;font-size:11px;color:var(--muted)}
.social span{display:flex;align-items:center;gap:8px}
.social i{width:30px;height:30px;border-radius:4px;display:block;background:var(--social)}

/* band */
.band{height:224px;background:linear-gradient(100deg,#4f9c2e,#62b03c 50%,#4f9c2e);color:var(--white);text-align:center;padding-top:68px}
.band h2{font-size:32px;font-weight:500}
.band-actions{display:flex;gap:16px;justify-content:center;margin-top:24px}
.band .now{background:var(--white);color:var(--ink);height:38px}
.band .how-to{border:1px solid var(--white);color:var(--white);height:38px}

/* footer */
.footer{height:568px;background:var(--footer);color:#c8ccd0;position:relative;padding:70px 90px 0}
.footer-cols{display:flex;justify-content:space-between}
.footer h2{font-size:22px;font-weight:500;color:var(--white)}
.footer-intro{font-size:12px;margin-top:16px;line-height:1.7;width:320px}
.contact-list{list-style:none;margin-top:34px}
.contact-list li{display:flex;gap:16px;font-size:12px;line-height:1.6;margin-bottom:26px}
.contact-list svg{flex:none;margin-top:2px}
.contact-form{width:510px}
.contact-form .footer-intro{width:auto}
.fields{display:flex;gap:12px;margin-top:30px}
.field{flex:1}
.field label{display:block;font-size:11px;color:var(--white);margin-bottom:8px}
.input{height:38px;background:var(--footer-field);font-size:11px;color:#8e959c;padding:0 14px;display:flex;align-items:center}
.message{height:130px;align-items:flex-start;padding-top:12px}
.submit{display:flex;justify-content:flex-end;margin-top:14px}
.submit .btn{background:var(--green);color:var(--white)}
.footer-bottom{position:absolute;left:90px;right:90px;bottom:14px;display:flex;justify-content:space-between;font-size:11px}
.footer-bottom nav{display:flex;gap:20px}
.to-top{position:absolute;right:30px;bottom:16px;width:40px;height:40px;border-radius:50%;background:var(--white);display:flex;align-items:center;justify-content:center}
</style>
</head>
<body>

<header>
  <div class="topbar">
    <div class="topbar-left">
      <span>
        <svg width="12" height="12" viewBox="0 0 24 24"><path fill="#6d737a" d="M6.6 10.8a15 15 0 006.6 6.6l2.2-2.2a1 1 0 011-.25 11.4 11.4 0 003.6.57 1 1 0 011 1V20a1 1 0 01-1 1A17 17 0 013 4a1 1 0 011-1h3.5a1 1 0 011 1c0 1.25.2 2.45.57 3.6a1 1 0 01-.25 1z"/></svg>
        Hotline: +1 555 014 2290
      </span>
      <span>
        <svg width="12" height="12" viewBox="0 0 24 24"><path fill="#6d737a" d="M2 5h20v14H2z M3 6l9 7 9-7" stroke="#fff" stroke-width="1.5"/></svg>
        Email: info@marrowfieldbrx.org
      </span>
    </div>
    <div class="topbar-right">
      <span>USD ▾</span>
      <span>ENGLISH ▾</span>
      <span><i class="dot"></i><i class="dot"></i><i class="dot"></i><i class="dot"></i></span>
    </div>
  </div>
  <div class="nav">
    <a class="brand" href="#"><i class="brand-mark"></i>MBRX</a>
    <nav class="menu">
      <a href="#">About us</a>
      <a href="#">Care &amp; Treatment</a>
      <a href="#">Research</a>
      <a href="#">Training</a>
      <a href="#">Get involved</a>
      <a href="#">Ways to give</a>
      <svg width="14" height="14" viewBox="0 0 24 24"><circle cx="10" cy="10" r="6.5" fill="none" stroke="#222831" stroke-width="2"/><path d="M15 15l6 6" stroke="#222831" stroke-width="2"/></svg>
      <svg width="14" height="14" viewBox="0 0 24 24"><circle cx="12" cy="8" r="5" fill="#222831"/><path d="M3 22a9 9 0 0118 0z" fill="#222831"/></svg>
      <a class="my-donation" href="#">My Donation $0.00</a>
      <svg width="20" height="16" viewBox="0 0 20 16"><path d="M0 2h20M0 8h20M0 14h20" stroke="#222831" stroke-width="2"/></svg>
    </nav>
  </div>
</header>

<section class="hero" role="img" aria-label="Photo of a smiling father holding his young son">
  <h1 class="hero-title">Marrowfield Biomedical<br>Research Institute</h1>
  <a class="btn" href="#">Why donate us</a>
  <div class="hero-dots"><i></i><i></i><i></i></div>
  <svg class="hero-curve" width="140" height="40" viewBox="0 0 140 40">
    <path d="M0 40C35 40 40 4 70 4s35 36 70 36z" fill="#fff"/>
    <circle cx="70" cy="24" r="13" fill="#fff" stroke="#222831" stroke-width="1.4"/>
    <path d="M64 21l6 6 6-6" fill="none" stroke="#222831" stroke-width="1.6"/>
  </svg>
</section>

<section class="how">
  <h2 class="heading">How it works</h2>
  <div class="heading-rule"></div>
  <div class="steps">
    <i class="connector" style="left:220px"></i>
    <i class="connector" style="left:520px"></i>
    <div class="step">
      <svg width="60" height="56" viewBox="0 0 60 56"><rect x="6" y="6" width="48" height="34" rx="2" fill="none" stroke="#1b75bb" stroke-width="2.5"/><path d="M22 50h16M30 40v10" stroke="#1b75bb" stroke-width="2.5"/><path d="M24 30c2-8 8-14 14-16-2 8-6 14-14 16z" fill="#5aa937"/></svg>
      <h3>Donate online</h3>
      <p>Give securely in a few steps and<br>support our research today.</p>
    </div>
    <div class="step">
      <svg width="60" height="56" viewBox="0 0 60 56"><rect x="6" y="12" width="48" height="32" fill="none" stroke="#1b75bb" stroke-width="2.5"/><path d="M6 12l24 18 24-18" fill="none" stroke="#5aa937" stroke-width="2.5"/></svg>
      <h3>Email your check</h3>
      <p>Send a scan of your check to our<br>team and we will process it.</p>
    </div>
    <div class="step">
      <svg width="60" height="56" viewBox="0 0 60 56"><circle cx="30" cy="28" r="22" fill="none" stroke="#1b75bb" stroke-width="2.5"/><path d="M19 28l8 8 18-20" fill="none" stroke="#5aa937" stroke-width="3"/></svg>
      <h3>Get confirmation</h3>
      <p>Receive a receipt by email for<br>every gift you make to us.</p>
    </div>
  </div>
</section>

<section class="ways">
  <h2 class="heading">These are the ways<br>you can donate to MBRX</h2>
  <div class="heading-rule"></div>
  <div class="cards">
    <article class="card">
      <div class="card-photo" role="img" aria-label="Photo of a white memorial building reflected in water at dusk" style="background:linear-gradient(180deg,#0d4f9c 0%,#3a86c9 45%,#123f70 60%,#0a2f5a 100%)"></div>
      <h3>Memorials &amp; dedications</h3>
      <p>Honor a loved one with a gift that funds new treatments and hope for patients.</p>
    </article>
    <article class="card">
      <div class="card-photo" role="img" aria-label="Photo of a person writing at a desk" style="background:linear-gradient(135deg,#d6d4d0,#9f9c98 60%,#7c7874)"></div>
      <div class="card-arrow"><svg width="14" height="14" viewBox="0 0 14 14"><path d="M2 7h10M8 3l4 4-4 4" fill="none" stroke="#222831" stroke-width="1.6"/></svg></div>
      <h3>Legacy and planned giving</h3>
      <p>Include our institute in your plans and shape research for years to come.</p>
    </article>
    <article class="card">
      <div class="card-photo" role="img" aria-label="Photo of two colleagues talking outdoors in warm sunlight" style="background:linear-gradient(135deg,#f2d48a,#b98a4a 45%,#4a5a38 100%)"></div>
      <h3>Give at work</h3>
      <p>Ask your employer to match gifts and double the impact of your support.</p>
    </article>
  </div>
  <a class="btn" href="#">Discover more ways to donate</a>
</section>

<section class="faq">
  <h2 class="heading">Frequently asked questions</h2>
  <div class="heading-rule"></div>
  <div class="faq-grid">
    <div class="faq-item"><h3>How is my donation used by the institute?</h3><p>Every gift funds research, new technologies and patient care programs. We report how funds are spent in our yearly review for all donors.</p></div>
    <div class="faq-item"><h3>Is my gift to the institute tax deductible?</h3><p>We are a registered non-profit and your gift may be deductible. A receipt is sent by email for each donation you make to us.</p></div>
    <div class="faq-item"><h3>Can I give in memory of a loved one?</h3><p>Yes, you can dedicate any gift and we will send a card to the family. Choose this option on the form when you donate.</p></div>
    <div class="faq-item"><h3>Can I set up a monthly recurring gift?</h3><p>Monthly giving helps us plan long term studies. You can change or cancel a recurring gift at any time from your account.</p></div>
  </div>
  <div class="faq-actions">
    <a class="btn more" href="#">View more questions</a>
    <a class="btn ask" href="#">Or ask your question</a>
  </div>
</section>

<section class="donate" role="img" aria-label="Photo of a smiling young man with a backpack looking at his phone on a city street">
  <div class="donate-box">
    <h2>Donate online</h2>
    <div class="heading-rule"></div>
    <p>Your online gift goes straight to our labs and clinics, helping us test new therapies and bring hope to patients faster.</p>
    <p>Giving takes only a minute and every amount makes a difference.</p>
    <a class="btn" href="#">Donate now</a>
  </div>
</section>

<section class="helping">
  <h2 class="heading">Helping terminally ill<br>patients worldwide</h2>
  <div class="heading-rule"></div>
  <div class="map" role="img" aria-label="Dotted world map with portraits of patients joined by green curved lines"></div>
  <div class="social">
    <span><i></i>@mbrx</span>
    <span><i></i>@mbrx</span>
    <span><i></i>@mbrx</span>
    <span><i></i>@mbrx</span>
  </div>
</section>

<section class="band">
  <h2>Your participation does matter</h2>
  <div class="band-actions">
    <a class="btn now" href="#">Donate now</a>
    <a class="btn how-to" href="#">How to donate</a>
  </div>
</section>

<footer class="footer">
  <div class="footer-cols">
    <div>
      <h2>Contact information</h2>
      <p class="footer-intro">If you need any further information you can visit us or contact us</p>
      <ul class="contact-list">
        <li><svg width="14" height="16" viewBox="0 0 24 24"><path d="M12 2a7 7 0 017 7c0 5-7 13-7 13S5 14 5 9a7 7 0 017-7z" fill="none" stroke="#5aa937" stroke-width="2"/><circle cx="12" cy="9" r="2.5" fill="#5aa937"/></svg><span>48 Alder Quay Road,<br>Brenmoor, Northland.</span></li>
        <li><svg width="14" height="14" viewBox="0 0 24 24"><path fill="#5aa937" d="M6.6 10.8a15 15 0 006.6 6.6l2.2-2.2a1 1 0 011-.25 11.4 11.4 0 003.6.57 1 1 0 011 1V20a1 1 0 01-1 1A17 17 0 013 4a1 1 0 011-1h3.5a1 1 0 011 1c0 1.25.2 2.45.57 3.6a1 1 0 01-.25 1z"/></svg><span>Telephone : +1 555 014 2290</span></li>
        <li><svg width="14" height="14" viewBox="0 0 24 24"><rect x="2" y="5" width="20" height="14" fill="none" stroke="#5aa937" stroke-width="2"/><path d="M2 5l10 8 10-8" fill="none" stroke="#5aa937" stroke-width="2"/></svg><span>Email : info@marrowfieldbrx.org</span></li>
        <li><svg width="14" height="14" viewBox="0 0 24 24"><circle cx="12" cy="12" r="10" fill="none" stroke="#5aa937" stroke-width="2"/><path d="M2 12h20M12 2c4 4 4 16 0 20M12 2c-4 4-4 16 0 20" fill="none" stroke="#5aa937" stroke-width="1.5"/></svg><span>Web : www.marrowfieldbrx.org</span></li>
      </ul>
    </div>
    <form class="contact-form">
      <h2>Contact form</h2>
      <p class="footer-intro">We are here for any kind of information and clarification.</p>
      <div class="fields">
        <div class="field"><label>Name</label><div class="input">Enter your name</div></div>
        <div class="field"><label>Email</label><div class="input">Enter your email address</div></div>
      </div>
      <div class="field" style="margin-top:16px"><label>Message</label><div class="input message">Enter your message</div></div>
      <div class="submit"><span class="btn">Submit</span></div>
    </form>
  </div>
  <div class="footer-bottom">
    <span>© 2017, All Rights Reserved</span>
    <nav><a href="#">Terms &amp; Conditions</a><span>|</span><a href="#">Privacy Policy</a></nav>
  </div>
  <a class="to-top" href="#"><svg width="14" height="14" viewBox="0 0 14 14"><path d="M7 12V2M3 6l4-4 4 4" fill="none" stroke="#222831" stroke-width="1.6"/></svg></a>
</footer>

</body>
</html>
```